Ridgeline Outfitters Business Cards

Recently had a logo done with Artfolio and now looking for a business card to go along with it.

Target Market(s)

Ridgeline Outfitters is a weapons dealer. My market will be primarily men, hunting, shooting type.

Industry/Entity Type

Business

Contact Information for Business Card

I selected double sided, but this is not required, single or double is going to be fine. I picture the logo on one side, or perhaps just the circle which contains "RO" with the remaining info on the other side.

Font styles to use
Sans Serif

Requirements
Must have
• My name: Milo Brandt
• Title: Owner
• tel: 612-555-0187
• web: www.ridgelineoutfittersmn.example
Nice to have
• I like the concept of a black business card. I would like to keep the colors monotone, black, grey, white or red. Red is acceptable because it is in the logo. I have also seen cards that are matte black with shiny black as well, perhaps for the logo (or circle RO) part of the logo.
• I will upload a couple of the logos for use, and also an example I just found of the black on black. and some others that have a nice contrast.
Should not have
• lots of colors are not wanted.

```html
<!DOCTYPE html>
<html lang="en">
<head>
<meta charset="utf-8">
<title>Ridgeline Outfitters – Business Card Print Sheet</title>
<link rel="stylesheet" href="https://fonts.googleapis.com/css2?family=Oswald:wght@500;700&display=swap">
<style>
  :root {
    --sheet: #ffffff;
    --crop: #3a3a3a;
    --card-charcoal: #222222;
    --card-black: #000000;
    --brand-red: #e3202a;
    --ring-grey: #7a7a7a;
    --ink-dark: #121212;
  }
  html, body {
    margin: 0;
    padding: 0;
    width: 816px;
    height: 1200px;
    overflow: hidden;
    background: var(--sheet);
  }
  .sheet {
    position: relative;
    width: 816px;
    height: 1200px;
    background: var(--sheet);
    font-family: "Oswald", "Arial Narrow", sans-serif;
  }
  .crop-marks {
    position: absolute;
    inset: 0;
  }
  .card {
    position: absolute;
    left: 122px;
    width: 572px;
    height: 327px;
    background: var(--card-charcoal);
    overflow: hidden;
  }
  .card--front { top: 122px; }
  .card--back { top: 750px; }
  .card__panel {
    position: absolute;
    top: 0;
    width: 196px;
    height: 100%;
    background: var(--card-black);
  }
  .card--front .card__panel { left: 0; }
  .card--back .card__panel { right: 0; }
  .emblem-ring {
    position: absolute;
    left: 50%;
    top: 50%;
    width: 112px;
    height: 112px;
    margin: -56px 0 0 -56px;
  }
  .wordmark {
    position: absolute;
    left: 196px;
    right: 0;
    top: 140px;
    margin: 0;
    text-align: center;
    color: var(--brand-red);
    font-weight: 700;
    font-size: 31px;
    letter-spacing: 1.5px;
    line-height: 1;
    text-transform: uppercase;
  }
  .contact {
    position: absolute;
    left: 30px;
    top: 0;
    bottom: 0;
    width: 330px;
    color: var(--ink-dark);
    font-weight: 700;
  }
  .contact__name {
    position: absolute;
    top: 24px;
    margin: 0;
    font-size: 22px;
    line-height: 1;
  }
  .contact__title {
    position: absolute;
    top: 48px;
    margin: 0;
    font-size: 14px;
    line-height: 1;
    font-weight: 500;
  }
  .contact__phone {
    position: absolute;
    top: 76px;
    margin: 0;
    font-size: 16px;
    line-height: 1;
  }
  .contact__web {
    position: absolute;
    top: 266px;
    margin: 0;
    font-size: 16px;
    line-height: 1.3;
  }
</style>
</head>
<body>
<main class="sheet">
  <svg class="crop-marks" width="816" height="1200" viewBox="0 0 816 1200" aria-hidden="true">
    <g stroke="var(--crop)" stroke-width="1">
      <line x1="122.5" y1="0" x2="122.5" y2="82"/>
      <line x1="693.5" y1="0" x2="693.5" y2="82"/>
      <line x1="122.5" y1="490" x2="122.5" y2="571"/>
      <line x1="693.5" y1="490" x2="693.5" y2="571"/>
      <line x1="122.5" y1="628" x2="122.5" y2="710"/>
      <line x1="693.5" y1="628" x2="693.5" y2="710"/>
      <line x1="122.5" y1="1118" x2="122.5" y2="1200"/>
      <line x1="693.5" y1="1118" x2="693.5" y2="1200"/>
      <line x1="0" y1="122.5" x2="82" y2="122.5"/>
      <line x1="734" y1="122.5" x2="816" y2="122.5"/>
      <line x1="0" y1="449.5" x2="82" y2="449.5"/>
      <line x1="734" y1="449.5" x2="816" y2="449.5"/>
      <line x1="0" y1="750.5" x2="82" y2="750.5"/>
      <line x1="734" y1="750.5" x2="816" y2="750.5"/>
      <line x1="0" y1="1077.5" x2="82" y2="1077.5"/>
      <line x1="734" y1="1077.5" x2="816" y2="1077.5"/>
    </g>
  </svg>

  <section class="card card--front" aria-label="Card front">
    <div class="card__panel">
      <svg class="emblem-ring" viewBox="0 0 112 112" aria-hidden="true">
        <circle cx="56" cy="56" r="52" fill="none" stroke="var(--ring-grey)" stroke-width="7"/>
      </svg>
    </div>
    <h1 class="wordmark">Ridgeline Outfitters</h1>
  </section>

  <section class="card card--back" aria-label="Card back">
    <div class="contact">
      <p class="contact__name">Milo Brandt</p>
      <p class="contact__title">owner</p>
      <p class="contact__phone">612-555-0187</p>
      <p class="contact__web">ridgelineoutfittersmn.example<br>info@ridgelineoutfittersmn.example</p>
    </div>
    <div class="card__panel">
      <svg class="emblem-ring" viewBox="0 0 112 112" aria-hidden="true">
        <circle cx="56" cy="56" r="52" fill="none" stroke="var(--ring-grey)" stroke-width="7"/>
      </svg>
    </div>
  </section>
</main>
</body>
</html>
```